Anzeigengestaltung für Reinigungsunternehmen
Zielgruppe
Wir sind ein Reinigungsunternehmen mit den Haupttätigkeitsfeldern: Büroreinigung, Treppenhausreinigung und Bauendreinigung.
Webseite: www.lorvapur.de
Die Zielgruppe sind Unternehmer (überwiegend Büros), Hausverwaltungen sowie Bauherren.
Aufgabenstellung
Die Reinigungsfirma wird mit dieser Anzeige zum ersten Mal beworben.
Umkreis: Kreis Paderborn und Kreis Gütersloh
Die Anzeige soll sowohl in Facebook beworben werden, sowie auch in den örtlichen Rundschauen.

```html
<!DOCTYPE html>
<html lang="de">
<head>
<meta charset="utf-8">
<title>Ostwald Glanz – Anzeigen</title>
<link href="https://fonts.googleapis.com/css2?family=Montserrat:wght@400;500;700;800&display=swap" rel="stylesheet">
<style>
:root{
  --stage:#d3d3d2;
  --white:#ffffff;
  --navy:#0a63a6;
  --sky:#0399d2;
  --green:#0aa63c;
  --brand-blue:#1f3fd6;
  --photo-office:linear-gradient(160deg,#e9eef2 0%,#b7c6d4 50%,#3a5f8c 100%);
  --photo-stairs:linear-gradient(160deg,#6b6b68 0%,#4a88d1 45%,#e8c234 75%,#3b3b38 100%);
  --photo-floor:linear-gradient(180deg,#8a8886 0%,#bdbbb9 40%,#f2f2f2 100%);
}
*{margin:0;padding:0;box-sizing:border-box}
html,body{width:1200px;height:1101px;overflow:hidden}
body{background:var(--stage);font-family:'Montserrat',sans-serif;position:relative}
.ad{position:absolute;box-shadow:0 8px 24px rgba(0,0,0,.18)}

/* Skyscraper */
.sky-ad{left:180px;top:167px;width:135px;height:766px}
.sky-ad .brand{height:76px;background:var(--white);display:flex;align-items:center;justify-content:center;gap:6px}
.brand-mark{width:12px;height:12px;background:var(--green);flex:none}
.brand-name{color:var(--brand-blue);font-weight:700;line-height:1.05}
.brand-owner{display:block;color:var(--brand-blue);font-weight:400}
.sky-ad .brand-name{font-size:13px}
.sky-ad .brand-owner{font-size:5px;margin-top:2px}
.sky-ad .intro{height:178px;background:var(--navy);color:var(--white);text-align:center;padding-top:17px}
.sky-ad .headline{font-size:14px;font-weight:400;line-height:16px}
.sky-ad .headline strong{font-weight:800}
.sky-ad .lead{font-size:8.5px;line-height:12px;margin-top:10px;padding:0 14px;font-weight:500}
.sky-ad .offers{height:436px;background:var(--sky);padding-top:19px;text-align:center}
.sky-ad .offers h2{color:var(--white);font-size:13px;font-weight:800;line-height:15px}
.sky-ad .offer-list{list-style:none;margin-top:16px}
.sky-ad .offer{position:relative;width:79px;height:106px;margin:0 auto 12px;border:4px solid var(--white)}
.sky-ad .offer .photo{width:100%;height:100%}
.sky-ad .offer .label{position:absolute;left:-7px;right:-7px;top:68px;background:var(--navy);color:var(--white);font-size:7.5px;font-weight:700;line-height:9px;padding:5px 2px;min-height:20px;display:flex;align-items:center;justify-content:center}
.sky-ad .cta{height:47px;background:var(--white);color:var(--navy);font-size:8px;font-weight:800;line-height:12px;text-align:center;display:flex;align-items:center;justify-content:center;padding:0 8px}
.sky-ad .url{height:29px;background:var(--green);color:var(--white);font-size:10px;font-weight:800;display:flex;align-items:center;justify-content:center}

/* Landscape */
.wide-ad{left:409px;top:370px;width:688px;height:361px}
.wide-ad .intro{position:absolute;left:0;top:0;width:295px;height:324px;background:var(--white);padding:23px 0 0 28px}
.wide-ad .brand{display:flex;align-items:center;gap:10px;height:60px}
.wide-ad .brand-mark{width:24px;height:24px}
.wide-ad .brand-name{font-size:24px}
.wide-ad .brand-owner{font-size:8px;margin-top:3px}
.wide-ad .headline{color:var(--navy);font-size:25px;font-weight:800;line-height:30px;margin-top:18px;white-space:nowrap}
.wide-ad .headline em{font-style:normal;color:var(--sky)}
.wide-ad .rule{width:74px;height:3px;background:var(--navy);margin-top:12px}
.wide-ad .lead{color:var(--navy);font-size:17.5px;line-height:24px;font-weight:500;margin-top:18px;white-space:nowrap}
.wide-ad .offers{position:absolute;left:295px;top:0;width:393px;height:324px;background:var(--sky)}
.wide-ad .offers h2{color:var(--white);font-size:24px;font-weight:800;text-align:center;margin-top:21px}
.wide-ad .offer-list{list-style:none;position:absolute;left:21px;top:78px;display:flex;gap:10px}
.wide-ad .offer{width:110px;display:flex;flex-direction:column;align-items:center}
.wide-ad .offer .photo{width:110px;height:178px;border:4px solid var(--white)}
.wide-ad .offer .label{height:50px;display:flex;align-items:center;color:var(--white);font-size:12.5px;font-weight:800;line-height:19px;text-align:center;white-space:nowrap;margin-top:8px}
.wide-ad .footer{position:absolute;left:0;bottom:0;width:688px;height:37px;display:flex}
.wide-ad .cta{width:465px;background:var(--navy);color:var(--white);font-size:15.5px;font-weight:800;display:flex;align-items:center;padding-left:30px}
.wide-ad .url{flex:1;background:var(--green);color:var(--white);font-size:15.5px;font-weight:800;display:flex;align-items:center;justify-content:center}

.photo-office{background:var(--photo-office)}
.photo-stairs{background:var(--photo-stairs)}
.photo-floor{background:var(--photo-floor)}
</style>
</head>
<body>

<section class="ad sky-ad">
  <header class="brand">
    <span class="brand-mark"></span>
    <span class="brand-name">Ostwald Glanz<span class="brand-owner">Inh. Jonas Brenner</span></span>
  </header>
  <div class="intro">
    <h1 class="headline">SCHENKEN<br>SIE IHREM<br><strong>OBJEKT</strong><br>NEUEN<br>GLANZ</h1>
    <p class="lead">Zuverlässige, professionelle Reinigungskräfte in Paderborn &amp; Gütersloh</p>
  </div>
  <div class="offers">
    <h2>UNSERE<br>ANGEBOTE</h2>
    <ul class="offer-list">
      <li class="offer"><div class="photo photo-office" role="img" aria-label="Reinigungskraft wischt den Boden eines Büros"></div><span class="label">Büroreinigung</span></li>
      <li class="offer"><div class="photo photo-stairs" role="img" aria-label="Putzwagen mit Eimer und Warnschild im Treppenhaus"></div><span class="label">Treppenhaus-<br>reinigung</span></li>
      <li class="offer"><div class="photo photo-floor" role="img" aria-label="Bodenreinigungsmaschine auf glänzenden Fliesen"></div><span class="label">Bauendreinigung</span></li>
    </ul>
  </div>
  <p class="cta">Für weitere Informationen besuchen Sie uns bitte</p>
  <p class="url">www.lorvapur.de</p>
</section>

<section class="ad wide-ad">
  <div class="intro">
    <header class="brand">
      <span class="brand-mark"></span>
      <span class="brand-name">Ostwald Glanz<span class="brand-owner">Inh. Jonas Brenner</span></span>
    </header>
    <h1 class="headline">SCHENKEN<br>SIE IHREM <em>OBJEKT</em><br>NEUEN GLANZ</h1>
    <div class="rule"></div>
    <p class="lead">Zuverlässige, professionelle<br>Reinigungskräfte in<br>Paderborn &amp; Gütersloh</p>
  </div>
  <div class="offers">
    <h2>Unsere Angebote</h2>
    <ul class="offer-list">
      <li class="offer"><div class="photo photo-office" role="img" aria-label="Reinigungskraft wischt den Boden eines Büros"></div><span class="label">Büroreinigung</span></li>
      <li class="offer"><div class="photo photo-stairs" role="img" aria-label="Putzwagen mit Eimer und Warnschild im Treppenhaus"></div><span class="label">Treppenhaus-<br>reinigung</span></li>
      <li class="offer"><div class="photo photo-floor" role="img" aria-label="Bodenreinigungsmaschine auf glänzenden Fliesen"></div><span class="label">Bauendreinigung</span></li>
    </ul>
  </div>
  <footer class="footer">
    <p class="cta">Für weitere Informationen besuchen Sie uns bitte</p>
    <p class="url">www.lorvapur.de</p>
  </footer>
</section>

</body>
</html>
```